New Wrestling company needs a website

We need a website design for a new wrestling company in Australia that will be running 3-4 events per year. Wrestling company is Coral Tide Grappling (CTG).

The design of the logo is in place and can be provided, and I have purchased the website domain.

A detailed description of the intent and purpose of this company can be provided.

The aim would be to have around 5 specific pages on CTG, with two standard “about” and “contact” pages. E.g.
- About CTG (focus and purpose of the company)
- CTG Events (specific focus on events run by CTG)
- CTG News (news and stories on wrestling’s across Oceania)
- CTG Media (where to watch CTG and our partners))
- CTG Partners and Sponsors (partner and affiliate information)
- CTG Power Rankings (top 10 ranked wrestlers from Oceania which is updated weekly)
- CTG fans (highlighting how to become part of CTG as a fan)
- Contact CTG
Updates

The logo design should now be included in the brief, please feel free to reach out to me directly if you can't access it or require any other information.

Target Market(s)

Wrestling Fans

Industry/Entity Type

Sport / Wrestling

Coding

Coded - Design and coding required

Number of Pages Required

5+ page

Requirements
Must have
• A Wrestling and or Sports feel to the website design

```html
<!DOCTYPE html>
<html lang="en">
<head>
<meta charset="utf-8">
<title>Coral Tide Grappling</title>
<link rel="stylesheet" href="https://fonts.googleapis.com/css2?family=Exo+2:wght@400;500;600;700&family=Roboto:wght@400;500;700&display=swap">
<style>
:root{
  --bg:#11273a;
  --bg-deep:#0b1a28;
  --footer:#0a141d;
  --blue:#2ea6ea;
  --blue-mid:#1f86d2;
  --blue-deep:#1a63b4;
  --white:#ffffff;
  --text:#e4edf5;
  --muted:#c2cfdb;
  --line:#2b8ad4;
}
*{margin:0;padding:0;box-sizing:border-box}
html,body{width:1200px;height:3711px;overflow:hidden}
body{
  position:relative;
  font-family:"Exo 2",sans-serif;
  color:var(--text);
  background:
    radial-gradient(ellipse 700px 500px at 600px 250px,#1d3a55 0%,transparent 70%),
    linear-gradient(180deg,#152f47 0%,var(--bg) 18%,#10263a 50%,#132b41 80%,var(--bg) 100%);
}
.abs{position:absolute}
.center{text-align:center}
.brand{font-family:"Exo 2",sans-serif;font-weight:700;color:var(--blue);display:flex;align-items:center;gap:8px}
.brand .dot{width:14px;height:14px;border-radius:50%;background:var(--blue);flex:none}

/* header */
.logo-top{left:99px;top:30px;font-size:15px;line-height:1.1;width:130px}
.nav{left:278px;top:39px;display:flex;gap:27px;font-family:"Roboto",sans-serif;font-size:10.5px;font-weight:700;letter-spacing:.3px;color:var(--white)}
.nav .active{color:var(--blue)}
.user-btn{left:936px;top:28px;width:38px;height:38px;border-radius:50%;background:var(--blue);display:flex;align-items:center;justify-content:center}
.contact-btn{left:988px;top:29px;width:111px;height:35px;border:1.5px solid var(--blue);border-radius:18px;font-family:"Roboto",sans-serif;font-size:10.5px;font-weight:700;color:var(--white);display:flex;align-items:center;justify-content:center}

/* hero */
.hero{left:99px;top:95px;width:1001px;height:435px;border:1.5px solid var(--blue-mid);
  background:linear-gradient(180deg,#4a4f57 0%,#3a3431 40%,#5a3a2d 70%,#2b2a2e 100%)}
.hero-shade{left:99px;top:330px;width:1001px;height:200px;background:linear-gradient(180deg,transparent,rgba(0,0,0,.45))}
.hero-title{left:99px;top:385px;width:1001px;font-family:"Roboto",sans-serif;font-weight:700;font-size:38px;color:var(--white)}
.hero-sub{left:99px;top:438px;width:1001px;font-family:"Roboto",sans-serif;font-weight:500;font-size:22px;color:var(--white)}
.slide-arrow{top:296px;width:30px;height:30px;border-radius:50%;background:var(--white);display:flex;align-items:center;justify-content:center}

/* common */
.h2{font-family:"Roboto",sans-serif;font-weight:500;font-size:33px;color:var(--white);letter-spacing:.5px}
.h2 .accent{color:var(--blue)}
.lead{font-size:15.5px;line-height:22px;color:var(--white)}
.lead .accent{color:var(--blue)}
.small{font-size:11px;line-height:22px;color:var(--muted)}
.pill{height:37px;border:1.5px solid var(--blue);border-radius:19px;font-family:"Roboto",sans-serif;font-size:10px;font-weight:700;letter-spacing:.5px;color:var(--white);display:flex;align-items:center;justify-content:center}
.pill.filled{background:linear-gradient(180deg,#2ea6ea,#1d74c6);border-color:#5cc1f5}

/* quote bands */
.quote-band{left:99px;width:1001px;height:139px;border-radius:90px 0 90px 0;
  background:linear-gradient(90deg,#1c66b8 0%,#2385d6 45%,#2fa8ec 100%);
  display:flex;align-items:center;justify-content:center;padding:0 130px}
.quote-band p{font-size:15px;line-height:18.5px;font-weight:500;color:var(--white);text-align:center}

/* events */
.event-list{left:200px;top:1226px;width:380px;list-style:none}
.event-list li{position:relative;padding-left:22px;font-size:12px;line-height:19px;color:var(--white);margin-bottom:18px}
.event-list li::before{content:"";position:absolute;left:0;top:4px;width:11px;height:11px;border-radius:50%;background:var(--blue)}
.event-brand{left:614px;top:1097px;width:384px;height:384px;display:flex;align-items:center;justify-content:center}
.event-brand .brand{font-size:44px;line-height:1.1;gap:18px}
.event-brand .dot{width:40px;height:40px}

/* partners */
.card{top:1879px;width:249px}
.card .photo{height:156px}
.card h3{margin-top:24px;font-size:15px;font-weight:500;line-height:19px;color:var(--blue)}
.card p{margin-top:14px;font-size:10px;line-height:19px;color:var(--muted)}
.card .more{margin-top:14px;font-family:"Roboto",sans-serif;font-size:10px;font-weight:700;color:var(--blue);letter-spacing:.5px}

/* media */
.media-box{top:2714px;width:249px;height:123px;border:1px solid #2c67a6;background:rgba(10,25,40,.35);display:flex;align-items:center;justify-content:center;padding:20px 22px 0;font-size:15px;font-weight:500;line-height:18.5px;color:var(--white);text-align:center}
.media-tag{top:2692px;width:249px;display:flex;justify-content:center}
.media-tag .brand{font-size:36px;background:var(--bg);padding:0 10px;line-height:44px}

/* fans */
.fans-photo{left:200px;top:2969px;width:388px;height:317px;background:linear-gradient(160deg,#6b5a52 0%,#3c2a26 45%,#7a2c28 75%,#241d1f 100%)}
.fans-text{left:612px;top:2962px;width:390px}
.fans-text p{font-size:10px;line-height:19px;color:var(--muted);margin-bottom:18px}

/* footer */
.footer{left:0;top:3355px;width:1200px;height:356px;background:var(--footer)}
.footer-logo{left:200px;top:3440px;font-size:30px;width:230px;line-height:1.05}
.footer h4{font-size:16px;font-weight:500;color:var(--blue)}
.links{display:grid;grid-template-columns:90px 120px;row-gap:10px;font-size:10.5px;color:var(--white)}
.email{left:749px;top:3462px;width:249px;height:35px;border:1px solid #3a6d9c;border-radius:18px;padding-left:17px;display:flex;align-items:center;font-size:10.5px;color:var(--white)}
.legal{left:200px;top:3617px;font-size:10.5px;color:var(--white);display:flex;gap:18px}
.legal .accent{color:var(--blue)}
.social{top:3607px;width:35px;height:35px;border-radius:50%;border:1px solid #2c67a6;display:flex;align-items:center;justify-content:center;font-size:8.5px;font-weight:600;color:var(--white)}
.social.on{background:var(--blue-mid);border-color:var(--blue)}
</style>
</head>
<body>

<!-- header -->
<div class="abs brand logo-top"><span class="dot"></span>Coral Tide Grappling</div>
<nav class="abs nav">
  <span class="active">HOME</span><span>ABOUT US</span><span>EVENTS</span><span>NEWS</span><span>MEDIA</span><span>PARTNERS &amp; SPONSORS</span><span>POWER RANKINGS</span><span>FANS</span>
</nav>
<div class="abs user-btn">
  <svg width="14" height="14" viewBox="0 0 14 14" fill="none" stroke="#fff" stroke-width="1.3"><circle cx="7" cy="4.5" r="2.5"/><path d="M2 13c0-3 2.2-4.5 5-4.5s5 1.5 5 4.5"/></svg>
</div>
<div class="abs contact-btn">CONTACT US</div>

<!-- hero -->
<div class="abs hero" role="img" aria-label="Wrestler celebrating on the ropes in a packed arena"></div>
<div class="abs hero-shade"></div>
<div class="abs hero-title center">LOREM IPSUM IS SIMPLY DUMMY TEXT</div>
<div class="abs hero-sub center">PRINTING AND TYPESETTING INDUSTRY IPSUM</div>
<div class="abs slide-arrow" style="left:84px"><svg width="10" height="10" viewBox="0 0 10 10" fill="none" stroke="#11273a" stroke-width="1.6"><path d="M6.5 1.5 3 5l3.5 3.5"/></svg></div>
<div class="abs slide-arrow" style="left:1085px"><svg width="10" height="10" viewBox="0 0 10 10" fill="none" stroke="#11273a" stroke-width="1.6"><path d="M3.5 1.5 7 5 3.5 8.5"/></svg></div>

<!-- welcome -->
<h2 class="abs h2 center" style="left:0;top:584px;width:1200px">WELCOME TO <span class="accent">CTG</span></h2>
<p class="abs lead center" style="left:205px;top:636px;width:790px;font-size:15px">Coral Tide Grappling (CTG) has been created as a <span class="accent">DESTINATION EVENT PRO WRESTLING</span> company for <span class="accent">OCEANIA.</span> We want to collaborate with other wrestling companies (Oceania and International) in our event, media and fan outcomes.</p>
<p class="abs small center" style="left:195px;top:719px;width:810px;color:var(--white)">The creator and Managing Director of CTG is an experienced and successful Australian Sporting Administrator with 20 plus years' experience in sport as a CEO and COO in three major Australian sports, and a deep passion for the wrestling industry.</p>
<div class="abs pill filled" style="left:536px;top:792px;width:127px">DISCOVER MORE</div>

<!-- quote 1 -->
<div class="abs quote-band" style="top:891px"><p>“The creator and Managing Director of CTG is an experienced and successful Australian Sporting Administrator with 20 plus years' experience in sport as a CEO and COO in three major Australian sports, and a deep passion for the wrestling industry.”</p></div>

<!-- events -->
<h2 class="abs h2" style="left:200px;top:1114px"><span class="accent">CTG</span> EVENTS</h2>
<p class="abs lead" style="left:200px;top:1166px;width:360px;font-size:15px;line-height:19px">The first CTG event will be announced in late March 2022.</p>
<ul class="abs event-list">
  <li>Putting on 3 to 4 key annual events in partnership with other wrestling companies, in locations in Oceania that seek to draw visitation to their cities.</li>
  <li>Giving Wrestling talent and wrestling promotions in Oceania an opportunity to shine.</li>
  <li>Commercially partner with leading international wrestling promotions.</li>
</ul>
<div class="abs pill" style="left:200px;top:1420px;width:124px;height:35px">EXPLORE MORE</div>
<div class="abs event-brand"><span class="brand"><span class="dot"></span>Coral Tide<br>Grappling</span></div>

<!-- quote 2 -->
<div class="abs quote-band" style="top:1547px"><p>“We are the bridge between the local promotions in Oceania to elevate their talent, and International promotions wanting to engage Oceania Fans with their international talent and brand.”</p></div>

<!-- partners -->
<h2 class="abs h2 center" style="left:0;top:1741px;width:1200px"><span class="accent">CTG</span> PARTNERS</h2>
<p class="abs lead center" style="left:0;top:1790px;width:1200px;font-size:15px">The first partners, internationally and Australian, are expected to be announced in late March 2022.</p>
<p class="abs small center" style="left:300px;top:1818px;width:600px;font-size:10.5px;line-height:15px;color:var(--white)">To our partners, companies or wrestling talent, CTG is about OPPORTUNITY – wrestling or business.<br>Wrestling partners will be from three key areas in our Event build.</p>

<div class="abs card" style="left:200px">
  <div class="photo" role="img" aria-label="Crowded ring of international wrestlers" style="background:linear-gradient(160deg,#7a6253,#3d2f2a 60%,#5a4a42)"></div>
  <h3>International Wrestling Organisations</h3>
  <p>We will look to partner with as many International Wrestling Companies for mutually beneficial outcomes, whether wrestling related…</p>
  <div class="more">READ MORE</div>
</div>
<div class="abs card" style="left:475px">
  <div class="photo" role="img" aria-label="Australian wrestling champions posing with a title belt" style="background:linear-gradient(160deg,#2d4f86,#4a3f5c 55%,#6a4f45)"></div>
  <h3>Australian Wrestling<br>Companies</h3>
  <p>Where possible we will elevate the talent and the promotions of the best Australian, NZ and other wrestling companies in Oceania…</p>
  <div class="more">READ MORE</div>
</div>
<div class="abs card" style="left:749px">
  <div class="photo" role="img" aria-label="Independent wrestlers in a match in the ring" style="background:linear-gradient(160deg,#8a2a2a,#4a2a28 55%,#6b5550)"></div>
  <h3>Free Agent Independent International Wrestlers</h3>
  <p>CTG events will be an opportunity for the strong base of international independent talent to appear as well.</p>
  <div class="more">READ MORE</div>
</div>
<div class="abs pill" style="left:537px;top:2233px;width:125px;height:35px">DISCOVER MORE</div>

<!-- quote 3 -->
<div class="abs quote-band" style="top:2333px"><p>“This combination will lead to 3-4 quality events per annum with an emphasis on showcasing professional wrestling through our quality broadcasting and highly engaging fan experience model at events, backed by a unique Membership model wrestling fans and a weekly media show”.</p></div>

<!-- media -->
<h2 class="abs h2 center" style="left:0;top:2528px;width:1200px"><span class="accent">CTG</span> MEDIA</h2>
<p class="abs lead center" style="left:250px;top:2578px;width:700px;font-size:15px;line-height:19px">CTG Media is anticipated to launch in June 2022, shortly after the announcement of our first major CTG event.</p>
<p class="abs small center" style="left:280px;top:2627px;width:640px;font-size:10.5px;line-height:18px;color:var(--white)">Between our events, we will seek to keep a consistent engagement via launching a new wrestling media show (TV, Radio or Podcast) to cover</p>

<div class="abs media-box" style="left:200px">Oceania talent in overseas promotions,</div>
<div class="abs media-box" style="left:475px">Oceania wrestling promotions and their local events and</div>
<div class="abs media-box" style="left:749px">CTG Events – the build to each CTG event and recap post event.</div>
<div class="abs media-tag" style="left:200px"><span class="brand">CTG</span></div>
<div class="abs media-tag" style="left:475px"><span class="brand">CTG</span></div>
<div class="abs media-tag" style="left:749px"><span class="brand">CTG</span></div>
<div class="abs pill filled" style="left:536px;top:2868px;width:127px">DISCOVER MEDIA</div>

<!-- fans -->
<div class="abs fans-photo" role="img" aria-label="Wrestler on the ring apron celebrating with a cheering crowd"></div>
<div class="abs fans-text">
  <h2 class="h2" style="font-size:32px"><span class="accent">CTG</span> FANS</h2>
  <p class="lead" style="font-size:15px;margin:14px 0 22px;color:var(--white)">CTG Membership will launch in July 2022.</p>
  <p>The core business is CTG Events, with supporting CTG Media and touring CTG champions.</p>
  <p>But the heartbeat of our events at CTG will be our CTG Fans – real fans of professional wrestling.</p>
  <p>Our aim at CTG is to create a sense of belonging to professional wrestling fans in Oceania through membership and engagement like it does for other sports and clubs in Australia.</p>
</div>
<div class="abs pill" style="left:612px;top:3249px;width:124px;height:35px">READ MORE</div>

<!-- footer -->
<footer class="abs footer"></footer>
<div class="abs brand footer-logo"><span class="dot" style="width:26px;height:26px"></span>Coral Tide Grappling</div>

<h4 class="abs footer-h" style="left:475px;top:3416px;font-size:16px;font-weight:500;color:var(--blue)">QUICK LINKS</h4>
<div class="abs links" style="left:475px;top:3456px">
  <span>Home</span><span>Partners &amp; Sponsors</span>
  <span>About Us</span><span>Power Ranking</span>
  <span>Events</span><span>Fans</span>
  <span>News</span><span>Contact Us</span>
  <span>Media</span><span></span>
</div>

<h4 class="abs" style="left:749px;top:3416px;font-size:16px;font-weight:500;color:var(--blue)">STAY IN TOUCH!</h4>
<div class="abs email">Enter Your Email...</div>
<div class="abs pill filled" style="left:749px;top:3514px;width:101px;height:37px">SUBMIT</div>

<div class="abs legal"><span>©2022 <span class="accent">CORAL TIDE GRAPPLING.</span> All Rights Reserved.</span><span>Privacy Policy</span><span>|</span><span>Terms of Use</span></div>

<div class="abs social" style="left:749px">Feed</div>
<div class="abs social on" style="left:794px">Chat</div>
<div class="abs social" style="left:838px">Pics</div>
<div class="abs social" style="left:882px">Clip</div>

<svg class="abs" style="left:1087px;top:3608px" width="24" height="28" viewBox="0 0 24 28" fill="none" stroke="#2ea6ea" stroke-width="2.2" stroke-linejoin="round"><path d="M12 2 22 26 12 19 2 26Z"/></svg>

</body>
</html>
```